Bref créative
Wedding photographer business card
and stationary
Bright & Fun-filled
Lora Bexley
no address needed
lorabexley@mailvista.net
www.lorabexley.net
I like sleek but also fun and feminine.
corrected phone number given to winning designer for finalizing design.
Thanks
Special offer,
$50 off,
a package & a free 8x10 print
I have two designs so you may choose either logo to design.
here's the monogram for my second logo
the flowers for logo 2

```html
<!DOCTYPE html>
<html lang="en">
<head>
<meta charset="utf-8">
<title>Lora Bexley Stationery Set</title>
<link href="https://fonts.googleapis.com/css2?family=Raleway:wght@400;600&display=swap" rel="stylesheet">
<style>
  :root {
    --backdrop: #eee8e0;
    --paper: #ffffff;
    --taupe: #c8b8a7;
    --taupe-dark: #a8978a;
    --rose: #c4414e;
    --rose-soft: #e39aa0;
    --ink: #6d6d6d;
    --line: #cfcfcf;
    --faint: #e6e6ea;
  }
  * { box-sizing: border-box; margin: 0; padding: 0; }
  html, body { width: 1200px; height: 660px; overflow: hidden; }
  body {
    background: var(--backdrop);
    font-family: "Raleway", sans-serif;
    color: var(--ink);
    position: relative;
  }
  .item { position: absolute; box-shadow: 0 2px 6px rgba(0,0,0,.15); }
  .paper { background: var(--paper); }
  .taupe { background: var(--taupe); }

  .brand-name {
    font-family: "Raleway", sans-serif;
    font-weight: 600;
    color: var(--rose);
    white-space: nowrap;
  }
  .flowers {
    position: absolute;
    border-radius: 40%;
    background: radial-gradient(circle at 40% 45%, var(--rose) 0%, var(--rose-soft) 45%, rgba(227,154,160,0) 72%);
  }

  /* business cards */
  .card { width: 144px; height: 84px; display: flex; flex-direction: column; align-items: center; justify-content: center; text-align: center; }
  .card .brand-name { font-size: 15px; }
  .card-contact { font-size: 6px; line-height: 1.5; margin-top: 6px; color: var(--ink); }
  .card.taupe .card-contact { color: #fff; }
  .card-contact.offer-foot { margin-top: 5px; }
  .offer-title { font-size: 12px; font-weight: 600; letter-spacing: .5px; }
  .offer-amount { font-size: 9px; margin-top: 2px; }
  .offer-detail { font-size: 7px; margin-top: 2px; }
  .card.taupe .offer-title, .card.taupe .offer-amount, .card.taupe .offer-detail { color: #fff; }
  .card.paper .offer-title { color: var(--ink); }

  /* fax sheet */
  .fax { left: 48px; top: 240px; width: 336px; height: 396px; padding: 26px 22px; }
  .fax .brand-name { display: block; text-align: center; font-size: 17px; }
  .fax-heading { text-align: right; font-size: 14px; font-weight: 600; margin-top: 14px; color: var(--ink); }
  .fax-fields { width: 100%; border-collapse: collapse; margin-top: 6px; font-size: 7px; }
  .fax-fields td { border: 1px solid var(--line); height: 17px; padding: 2px 4px; vertical-align: top; }
  .fax-fields td.label { width: 34px; }
  .fax-checks { display: flex; justify-content: space-between; margin-top: 10px; font-size: 6.5px; }
  .fax-checks span::before { content: ""; display: inline-block; width: 7px; height: 7px; border: 1px solid var(--ink); margin-right: 3px; vertical-align: -1px; }
  .sheet-footer { position: absolute; bottom: 14px; left: 0; right: 0; text-align: center; font-size: 6px; }

  /* letterhead */
  .letterhead { left: 408px; top: 240px; width: 312px; height: 396px; overflow: hidden; }
  .watermark {
    position: absolute; left: 0; right: 0; top: 96px;
    text-align: center; font-size: 76px; line-height: 1.05;
    color: var(--faint);
  }
  .letterhead .sign-name { position: absolute; left: 18px; bottom: 30px; font-size: 11px; }
  .letterhead .sheet-footer { left: 18px; text-align: left; bottom: 14px; }

  /* envelopes */
  .envelope { width: 410px; height: 146px; overflow: hidden; }
  .env-front { left: 742px; top: 48px; }
  .env-front .brand-name { position: absolute; left: 100px; top: 34px; font-size: 14px; }
  .env-band { position: absolute; left: 0; right: 0; bottom: 0; height: 58px; background: var(--taupe); }
  .env-band .sheet-footer { color: #fff; bottom: 8px; }
  .env-second { left: 742px; top: 250px; }
  .env-second .brand-name { position: absolute; left: 96px; top: 30px; font-size: 14px; }
  .env-back { left: 742px; top: 440px; }
  .env-back svg { position: absolute; inset: 0; }
  .env-back .brand-name { position: absolute; left: 0; right: 0; text-align: center; top: 58px; font-size: 13px; }
  .env-back .sheet-footer { bottom: 10px; color: #fff; }
</style>
</head>
<body>

  <!-- business cards -->
  <div class="item card paper" style="left:84px; top:60px;">
    <span class="brand-name">Lora Bexley</span>
    <div class="card-contact">lorabexley@mailvista.net<br>www.lorabexley.net</div>
  </div>
  <div class="item card taupe" style="left:240px; top:60px;">
    <div class="offer-title">SPECIAL OFFER</div>
    <div class="offer-amount">$50 off</div>
    <div class="offer-detail">a package &amp; a free 8x10 print</div>
    <div class="card-contact offer-foot">www.lorabexley.net</div>
  </div>
  <div class="item card taupe" style="left:408px; top:78px;">
    <span class="brand-name" style="color:#fff">Lora Bexley</span>
    <div class="card-contact">lorabexley@mailvista.net<br>www.lorabexley.net</div>
  </div>
  <div class="item card paper" style="left:570px; top:38px;">
    <div class="offer-title">SPECIAL OFFER</div>
    <div class="offer-amount">$50 off</div>
    <div class="offer-detail">a package &amp; a free 8x10 print</div>
    <div class="card-contact offer-foot">www.lorabexley.net</div>
  </div>

  <!-- fax sheet -->
  <section class="item paper fax">
    <span class="brand-name">Lora Bexley</span>
    <div class="fax-heading">Fax</div>
    <table class="fax-fields">
      <tr><td class="label">To:</td><td></td><td class="label">From:</td><td></td></tr>
      <tr><td class="label">Fax:</td><td></td><td class="label">Pages:</td><td></td></tr>
      <tr><td class="label">Phone:</td><td></td><td class="label">Date:</td><td></td></tr>
      <tr><td class="label">Re:</td><td></td><td class="label">CC:</td><td></td></tr>
    </table>
    <div class="fax-checks">
      <span>Urgent</span><span>For Review</span><span>Please Comment</span><span>Please Reply</span><span>Please Recycle</span>
    </div>
    <div class="sheet-footer">lorabexley@mailvista.net &nbsp;|&nbsp; www.lorabexley.net</div>
  </section>

  <!-- letterhead -->
  <section class="item paper letterhead">
    <div class="flowers" role="img" aria-label="Red rose and swirl floral ornament" style="right:-10px; top:6px; width:120px; height:60px;"></div>
    <div class="watermark brand-name">Lora<br>Bexley</div>
    <div class="flowers" role="img" aria-label="Red rose floral ornament" style="right:4px; bottom:14px; width:120px; height:56px;"></div>
    <span class="brand-name sign-name">Lora Bexley</span>
    <div class="sheet-footer">lorabexley@mailvista.net &nbsp;|&nbsp; www.lorabexley.net</div>
  </section>

  <!-- envelopes -->
  <section class="item paper envelope env-front">
    <div class="flowers" role="img" aria-label="Red rose and swirl floral ornament" style="left:6px; top:10px; width:96px; height:56px;"></div>
    <span class="brand-name">Lora Bexley</span>
    <div class="env-band"><div class="sheet-footer">lorabexley@mailvista.net &nbsp;|&nbsp; www.lorabexley.net</div></div>
  </section>

  <section class="item paper envelope env-second">
    <div class="flowers" role="img" aria-label="Red rose and swirl floral ornament" style="left:6px; top:6px; width:92px; height:54px;"></div>
    <span class="brand-name">Lora Bexley</span>
  </section>

  <section class="item taupe envelope env-back">
    <svg width="410" height="146" viewBox="0 0 410 146" aria-hidden="true">
      <polygon points="0,0 410,0 205,100" fill="#ffffff"/>
      <polygon points="0,0 205,100 410,0" fill="none" stroke="#a8978a" stroke-width="1"/>
    </svg>
    <span class="brand-name">Lora Bexley</span>
    <div class="sheet-footer">lorabexley@mailvista.net</div>
  </section>

</body>
</html>
```